依頼詳細
A4サイズカラー両面チラシのデザイン
・光触媒コーティングサービスのメリットが伝わるもの
・イラストを使用して、わかりやすいもの
※チラシデザインを決定させていただき、それをベースにLPデザインも追加依頼予定(別途料金)
記載項目
株式会社Sorano Works
山口県山口市小郡若葉町3-17
TEL 083-512-4937
サイズ
A4
ページ数
両面
希望イメージ
シンプル 複雑
単色 カラフル
暗い 明るい
日常 高級
遊び心 厳粛
未来的 伝統的
女性的 男性的
希望する色
黄・オレンジ系、緑系、青系
納品ファイル
• イラストレーター形式 (.ai)
■ 選んだ理由

完成イメージに近かったです。

■ 提案者全員のお礼・コメント

皆様、ご提案ありがとうございました。

```html
<!DOCTYPE html>
<html lang="ja">
<head>
<meta charset="UTF-8">
<title>光触媒コーティング</title>
<link href="https://fonts.googleapis.com/css2?family=Noto+Sans+JP:wght@400;700;900&family=M+PLUS+Rounded+1c:wght@800;900&display=swap" rel="stylesheet">
<style>
:root{
  --orange:#f08a1c;
  --orange-deep:#e46a10;
  --blue:#2a86d6;
  --blue-deep:#1b5fae;
  --sky:#e6f3fb;
  --ink:#2b2b2b;
  --red:#e8272c;
  --white:#ffffff;
}
*{margin:0;padding:0;box-sizing:border-box}
html,body{width:851px;height:1200px;overflow:hidden;background:#fff}
body{font-family:"Noto Sans JP",sans-serif;color:var(--ink)}
.flyer{position:relative;width:851px;height:1200px;overflow:hidden;background:linear-gradient(#fff 0,#fff 460px,var(--sky) 460px,var(--sky) 765px,#fff 765px)}
.hero-photo{position:absolute;left:0;top:0;width:851px;height:490px;background:linear-gradient(180deg,#f4efe4 0%,#eadcc4 55%,#d7b88e 100%)}
.virus-badge{position:absolute;left:660px;top:262px;width:168px;height:168px;border-radius:50%;background:var(--white);border:4px solid #f6c59a;text-align:center;padding-top:28px;color:var(--orange-deep);font-weight:700;line-height:1.15}
.virus-badge .label{font-size:15px;color:var(--ink)}
.virus-badge .rate{font-size:40px;font-weight:900;color:var(--orange-deep);letter-spacing:-1px}
.virus-badge .down{font-size:22px;font-weight:900}
.headline{position:absolute;left:60px;top:460px;display:flex;align-items:center;gap:14px}
.headline .tag{background:linear-gradient(var(--orange),var(--orange-deep));color:#fff;font-size:54px;font-weight:900;padding:0 16px;line-height:76px;border-radius:6px;border:3px solid #fff;box-shadow:0 2px 0 rgba(0,0,0,.15)}
.headline .ask{font-size:36px;font-weight:900;color:var(--ink);line-height:1.1}
.title{position:absolute;left:0;width:851px;top:560px;text-align:center;font-family:"M PLUS Rounded 1c",sans-serif;font-weight:900;font-size:88px;line-height:1;color:var(--orange);-webkit-text-stroke:3px #fff;paint-order:stroke fill;text-shadow:0 4px 0 #f6c59a;white-space:nowrap}
.title .lead{color:#fff;-webkit-text-stroke:3px var(--orange)}
.effects{position:absolute;left:32px;top:670px;width:787px;display:flex;justify-content:space-between}
.effects li{list-style:none;width:148px;height:56px;border-radius:28px;background:linear-gradient(#4aa6ea,var(--blue-deep));color:#fff;font-size:29px;font-weight:900;display:flex;align-items:center;justify-content:center}
.targets{position:absolute;left:0;width:851px;top:738px;text-align:center;font-size:14px;font-weight:700;color:var(--ink);white-space:nowrap}
.merits{position:absolute;left:28px;top:776px;width:450px}
.merits h2{font-size:21px;font-weight:900;color:var(--orange-deep);border-bottom:3px solid var(--orange);padding-bottom:4px;margin-bottom:8px}
.merits ul{list-style:none}
.merits li{display:flex;align-items:center;gap:10px;font-size:19px;font-weight:700;height:46px;border-bottom:1px dashed #c9c9c9;white-space:nowrap}
.merits li em{font-style:normal;color:var(--orange-deep)}
.merits svg{flex:none}
.office-photo{position:absolute;left:500px;top:800px;width:351px;height:262px;background:linear-gradient(160deg,#eef1f4 0%,#c9d2db 60%,#9aa7b3 100%)}
.quote{position:absolute;left:690px;top:900px;width:134px;height:100px;border-radius:12px;background:var(--white);border:3px solid var(--orange);text-align:center;padding-top:10px}
.quote .q1{font-size:20px;font-weight:900;color:var(--ink)}
.quote .q2{font-size:38px;font-weight:900;color:var(--red);line-height:1.1}
.staff{position:absolute;left:700px;top:1010px;width:151px;height:190px;background:linear-gradient(#f7d9c0,#cfe6f6)}
.catch{position:absolute;left:28px;top:1068px;font-size:22px;font-weight:900;color:var(--blue-deep);white-space:nowrap}
.catch em{font-style:normal;color:var(--red)}
.price-row{position:absolute;left:28px;top:1106px;width:660px;height:90px;display:flex;align-items:center;gap:12px;border-top:3px solid var(--blue);white-space:nowrap}
.plan{font-size:17px;font-weight:700;line-height:1.25;color:var(--blue-deep);text-align:center}
.plan small{display:block;font-size:13px;color:var(--ink)}
.price{font-size:72px;font-weight:900;color:var(--red);letter-spacing:-2px;line-height:1;display:flex;align-items:flex-end}
.price .yen{font-size:40px;margin-left:2px}
.price .tax{font-size:17px;color:var(--ink);letter-spacing:0;align-self:flex-start;margin-left:4px;margin-top:4px}
</style>
</head>
<body>
<div class="flyer">
  <div class="hero-photo" role="img" aria-label="明るい保育室で先生と子どもたちが手をつないで遊ぶ写真"></div>
  <div class="virus-badge">
    <div class="label">A型<br>インフルエンザ<br>ウイルス</div>
    <div class="rate">99.9%</div>
    <div class="down">減少</div>
  </div>

  <div class="headline">
    <span class="tag">脱臭</span>
    <span class="tag">除菌</span>
    <span class="ask">対策<br>してますか？</span>
  </div>

  <h1 class="title"><span class="lead">光触媒</span>コーティング</h1>

  <ul class="effects">
    <li>防カビ</li><li>抗菌</li><li>除菌</li><li>防臭</li><li>防汚</li>
  </ul>
  <p class="targets">【インフルエンザウイルス、ノロウイルス、O-157、真菌、水虫菌、黄色ブドウ球菌などの除菌・抗菌が可能です。】</p>

  <section class="merits">
    <h2>進化した光触媒超微粒子酸化チタン</h2>
    <ul>
      <li><svg width="24" height="24" viewBox="0 0 24 24"><rect x="2" y="4" width="18" height="18" fill="#fff" stroke="#1b5fae" stroke-width="2"/><path d="M6 12l5 5 11-14" fill="none" stroke="#e46a10" stroke-width="3"/></svg>都度のアルコール消毒等も<em>必要がない</em></li>
      <li><svg width="24" height="24" viewBox="0 0 24 24"><rect x="2" y="4" width="18" height="18" fill="#fff" stroke="#1b5fae" stroke-width="2"/><path d="M6 12l5 5 11-14" fill="none" stroke="#e46a10" stroke-width="3"/></svg>一度の噴霧で<em>長時間抗菌</em></li>
      <li><svg width="24" height="24" viewBox="0 0 24 24"><rect x="2" y="4" width="18" height="18" fill="#fff" stroke="#1b5fae" stroke-width="2"/><path d="M6 12l5 5 11-14" fill="none" stroke="#e46a10" stroke-width="3"/></svg>ウイルスを<em>分解・不活性化</em></li>
      <li><svg width="24" height="24" viewBox="0 0 24 24"><rect x="2" y="4" width="18" height="18" fill="#fff" stroke="#1b5fae" stroke-width="2"/><path d="M6 12l5 5 11-14" fill="none" stroke="#e46a10" stroke-width="3"/></svg>効果は<em>数年持続！</em></li>
      <li><svg width="24" height="24" viewBox="0 0 24 24"><rect x="2" y="4" width="18" height="18" fill="#fff" stroke="#1b5fae" stroke-width="2"/><path d="M6 12l5 5 11-14" fill="none" stroke="#e46a10" stroke-width="3"/></svg>防カビ・防汚作用で<em>お手入れも簡単！</em></li>
    </ul>
  </section>

  <div class="office-photo" role="img" aria-label="明るいオフィスのデスクが並ぶ室内写真"></div>
  <div class="quote"><div class="q1">お見積り</div><div class="q2">無料</div></div>
  <div class="staff" role="img" aria-label="作業服姿のスタッフのイラスト"></div>

  <p class="catch">革新的な抗菌＆除菌で<em>低価格化</em>を実現</p>
  <div class="price-row">
    <svg width="64" height="64" viewBox="0 0 70 70" aria-hidden="true">
      <rect x="10" y="24" width="34" height="14" rx="3" fill="#1b5fae"/>
      <rect x="44" y="28" width="14" height="6" fill="#1b5fae"/>
      <rect x="20" y="38" width="10" height="24" rx="2" fill="#2a86d6"/>
      <rect x="16" y="8" width="18" height="16" rx="3" fill="#2a86d6"/>
      <circle cx="63" cy="24" r="2" fill="#2a86d6"/><circle cx="66" cy="31" r="2" fill="#2a86d6"/><circle cx="63" cy="38" r="2" fill="#2a86d6"/>
    </svg>
    <div class="plan">6帖間<br>スプレーガン噴霧<small>（床／壁／天井）</small></div>
    <div class="price">39,000<span class="yen">円~</span><span class="tax">(税別)</span></div>
  </div>
</div>
</body>
</html>
```